Body therapist needs a business card

I need a card for my business which is teaching trainings in body therapy, the company is called Wexcombe Educational Group. I teach to massage therapists around Australia, South East Asia and the USA. I am attaching my logo which will guide you as to what colours I would like to have you consider. Please consult my website to find out more about what I do. www.corvantela.com.au

My name is Daniel Wexcombe. My phone number is (03) 9417 2608 or 0461753208. email is info@corvantela.com.au

```html
<!DOCTYPE html>
<html lang="en">
<head>
<meta charset="utf-8">
<title>Wexcombe Educational Group — Business Card</title>
<link rel="stylesheet" href="https://fonts.googleapis.com/css2?family=Fira+Sans:wght@300;400&display=swap">
<style>
  :root {
    --page-bg: #ececec;
    --card-white: #ffffff;
    --card-outline: #222222;
    --brand-brown: #7d3819;
    --brand-brown-dark: #6e3015;
    --brand-brown-faint: #8a4322;
    --brand-lime: #c5d62c;
    --text-brown: #8b4a2a;
    --text-light: #f3e9e2;
  }
  * { margin: 0; padding: 0; box-sizing: border-box; }
  html, body {
    width: 1200px;
    height: 1200px;
    overflow: hidden;
    background: var(--page-bg);
    font-family: "Fira Sans", sans-serif;
  }
  .canvas { position: relative; width: 1200px; height: 1200px; }
  .card {
    position: absolute;
    left: 356px;
    width: 473px;
    height: 267px;
  }
  .card--front {
    top: 154px;
    background: var(--card-white);
    border: 1px solid var(--card-outline);
  }
  .card--back {
    top: 747px;
    background: var(--brand-brown);
    overflow: hidden;
  }
  .brand-mark {
    position: absolute;
    left: 121px;
    top: 100px;
    width: 78px;
    height: 78px;
    border-radius: 50%;
    background: var(--brand-brown);
  }
  .brand-name {
    position: absolute;
    left: 208px;
    top: 118px;
    color: var(--text-brown);
    font-weight: 300;
    line-height: 1;
  }
  .brand-name__main { display: block; font-size: 26px; }
  .brand-name__sub { display: block; font-size: 11px; margin-top: 5px; }
  .back-mark {
    position: absolute;
    left: 200px;
    top: 99px;
    width: 70px;
    height: 70px;
    border-radius: 50%;
    background: var(--brand-brown-faint);
  }
  .rule {
    position: absolute;
    left: 0;
    right: 0;
    top: 219px;
    height: 1px;
    background: var(--brand-brown-dark);
  }
  .holder-name {
    position: absolute;
    left: 0;
    right: 0;
    top: 202px;
    text-align: center;
    font-size: 25px;
    font-weight: 300;
    color: var(--text-light);
    line-height: 1.2;
  }
  .contacts {
    position: absolute;
    left: 0;
    right: 0;
    top: 237px;
    display: flex;
    justify-content: center;
    gap: 12px;
    font-size: 10px;
    font-weight: 300;
    color: var(--brand-lime);
  }
  .contact { display: flex; align-items: center; gap: 3px; }
  .contact svg { width: 11px; height: 11px; fill: var(--brand-lime); }
</style>
</head>
<body>
<main class="canvas">
  <section class="card card--front" aria-label="Card front">
    <div class="brand-mark"></div>
    <div class="brand-name">
      <span class="brand-name__main">Wexcombe</span>
      <span class="brand-name__sub">Educational Group</span>
    </div>
  </section>

  <section class="card card--back" aria-label="Card back">
    <div class="back-mark"></div>
    <div class="rule"></div>
    <p class="holder-name">Daniel Wexcombe</p>
    <div class="contacts">
      <span class="contact">
        <svg viewBox="0 0 24 24" aria-hidden="true"><path d="M6.6 10.8a15.1 15.1 0 0 0 6.6 6.6l2.2-2.2a1 1 0 0 1 1-.25 11.4 11.4 0 0 0 3.6.57 1 1 0 0 1 1 1V20a1 1 0 0 1-1 1A17 17 0 0 1 3 4a1 1 0 0 1 1-1h3.5a1 1 0 0 1 1 1c0 1.25.2 2.45.57 3.57a1 1 0 0 1-.25 1z"/></svg>
        (03) 9417 2608, 0461753208
      </span>
      <span class="contact">
        <svg viewBox="0 0 24 24" aria-hidden="true"><path d="M2 5h20v14H2z M3.5 6.5 12 13l8.5-6.5" stroke="#7d3819" stroke-width="1.2"/></svg>
        info@corvantela.com.au
      </span>
      <span class="contact">
        <svg viewBox="0 0 24 24" aria-hidden="true"><circle cx="12" cy="12" r="10"/><path d="M2 12h20M12 2c3 3 3 17 0 20M12 2c-3 3-3 17 0 20" stroke="#7d3819" stroke-width="1.2" fill="none"/></svg>
        www.corvantela.com.au
      </span>
    </div>
  </section>
</main>
</body>
</html>
```